Looking for a cutting-edge design for a healthy, all-nautural dog treats package

We are launching an All-Natural dog treat. It is made of 5 simple ingredients (peanut butter, sweet potatoes, potato flour, flaxseed oil & eggs). This product is white-labeled (meaning the original manufacturer will be producing them for us under our own name). The brand name is TrailHop.

What We Are Looking For:
We are looking for an approach that really emphasizes the fact that it will be all-natural, grain-free. In fact, we are looking for a design that is very similar to the qu loaf (please take a look at quloafdemo.net for examples).

Other Details to Remember:
Attached is a png file of the dimensions provided by the original manufacturer. Please note that our bag will the a "brown paper bag" color. Finally, the back of the bag should include the same verbiage as the original (although does not have to be the same design/fonts).
Updates

Project Deadline Extended Reason: It appears that the package can now only be in one color on "brown paper bag" of "off white" packaging. Added Wednesday, October 26, 2016

Target Market(s)

Dog owners that appreciate quality food for their pets...more than likely, they are foodies themselves and/or health conscience

Industry/Entity Type

Pet

Logo Text

TrailHop

Requirements
Must have
• Emphasis on the product being all-natural, grain-free. Looks similar to the quloaf packaging (quloafdemo.net)
• **IMPORTANT UPDATE**
• The packaging people have notified us that all graphics or lettering must be in ONE SAME COLOR. The package itself will be in either "brown paper bag" or "off white" color.
Should not have
• That being said, please do NOT make it look absolutely identical to the qu loaf

```html
<!DOCTYPE html>
<html lang="en">
<head>
<meta charset="UTF-8">
<title>TrailHop Grain Free Treats – Pouch Front</title>
<link rel="stylesheet" href="https://fonts.googleapis.com/css2?family=Oswald:wght@500;700&display=swap">
<style>
  :root {
    --page: #ffffff;
    --kraft: #c69c6d;
    --kraft-shade: #b98d5e;
    --ink: #1b1612;
    --band-dark: #3a2c20;
    --band-light: #5a4432;
    --treat-dark: #6b3d1c;
    --treat-light: #a8652e;
  }
  html, body {
    margin: 0;
    padding: 0;
    width: 906px;
    height: 1200px;
    overflow: hidden;
    background: var(--page);
  }
  .pouch-front {
    display: block;
    width: 906px;
    height: 1200px;
  }
  .pouch-body { fill: var(--kraft); }
  .seal-line { stroke: var(--kraft-shade); stroke-width: 2; fill: none; }
  .ink-stroke { fill: none; stroke: var(--ink); }
  .ink-fill { fill: var(--ink); }
  .panel { fill: var(--kraft); stroke: var(--ink); stroke-width: 4; }
  .brand-name {
    font-family: "Oswald", sans-serif;
    font-weight: 700;
    font-size: 32px;
    letter-spacing: 2px;
    fill: var(--ink);
  }
  .badge-text {
    font-family: "Oswald", sans-serif;
    font-weight: 500;
    font-size: 11px;
    letter-spacing: 0.5px;
    fill: var(--kraft);
  }
  .ingredient {
    font-family: "Oswald", sans-serif;
    font-weight: 700;
    font-size: 25px;
    fill: var(--ink);
  }
  .net-weight {
    font-family: "Oswald", sans-serif;
    font-weight: 700;
    font-size: 13px;
    fill: var(--ink);
  }
</style>
</head>
<body>
<svg class="pouch-front" viewBox="0 0 906 1200" xmlns="http://www.w3.org/2000/svg">
  <defs>
    <linearGradient id="treat-tone" x1="0" y1="0" x2="1" y2="1">
      <stop offset="0" stop-color="var(--treat-light)"/>
      <stop offset="0.5" stop-color="var(--treat-dark)"/>
      <stop offset="1" stop-color="var(--treat-light)"/>
    </linearGradient>
    <linearGradient id="band-tone" x1="0" y1="0" x2="0" y2="1">
      <stop offset="0" stop-color="var(--band-dark)"/>
      <stop offset="1" stop-color="var(--band-light)"/>
    </linearGradient>
  </defs>

  <!-- pouch face -->
  <rect class="pouch-body" x="252" y="274" width="458" height="674" rx="6"/>
  <line class="seal-line" x1="252" y1="352" x2="710" y2="352"/>

  <!-- emblem frame: outer outline with a flat decorative band -->
  <path d="M334,760 L334,474 Q334,462 346,458 L392,444 Q480,364 568,444 L614,458 Q628,462 628,474 L628,760 Z"
    fill="url(#band-tone)" stroke="var(--ink)" stroke-width="5"
    role="img" aria-label="Decorative striped sunburst band framing the label"/>

  <!-- ingredient panel -->
  <rect class="panel" x="382" y="500" width="196" height="252"/>

  <!-- mascot medallion -->
  <ellipse cx="480" cy="428" rx="58" ry="36" fill="var(--kraft)" stroke="var(--ink)" stroke-width="5"/>
  <ellipse cx="480" cy="428" rx="46" ry="26" fill="var(--band-light)"
    role="img" aria-label="Mascot illustration of a small dog flanked by hearts"/>

  <!-- brand ribbon -->
  <path class="panel" stroke-width="3"
    d="M322,494 Q480,456 652,472 L656,520 Q480,504 328,538 Z"/>
  <text class="brand-name" x="488" y="513" text-anchor="middle">TrailHop</text>

  <!-- grain free badge -->
  <rect class="ink-fill" x="438" y="522" width="84" height="17" rx="8.5"/>
  <text class="badge-text" x="480" y="535" text-anchor="middle">GRAIN FREE</text>

  <!-- ingredient list -->
  <g class="ingredient-list">
    <line class="ink-stroke" stroke-width="2" x1="384" y1="585" x2="576" y2="585"/>
    <line class="ink-stroke" stroke-width="2" x1="384" y1="627" x2="576" y2="627"/>
    <line class="ink-stroke" stroke-width="2" x1="384" y1="668" x2="576" y2="668"/>
    <line class="ink-stroke" stroke-width="2" x1="384" y1="708" x2="576" y2="708"/>
    <text class="ingredient" x="480" y="574" text-anchor="middle">PEANUT BUTTER</text>
    <text class="ingredient" x="480" y="616" text-anchor="middle">SWEET POTATOES</text>
    <text class="ingredient" x="480" y="658" text-anchor="middle">POTATO FLOUR</text>
    <text class="ingredient" x="480" y="698" text-anchor="middle">FLAXSEED OIL</text>
    <text class="ingredient" x="480" y="738" text-anchor="middle">EGGS</text>
  </g>

  <!-- product window -->
  <rect x="322" y="772" width="316" height="88" rx="14" fill="url(#treat-tone)"
    stroke="var(--ink)" stroke-width="3"
    role="img" aria-label="Clear window showing the baked peanut butter dog treats inside"/>

  <text class="net-weight" x="480" y="892" text-anchor="middle">NET WT. 1.83 OZ (52g)</text>
</svg>
</body>
</html>
```